Sumvane financial services stationery design

We need business stationery designed with letterheads, business cards, with compliments and envelope for a business that offers tax and accounting services

Designs look the same

Target Market(s)

Small to medium businesses, individuals, Self managed superfunds

Industry/Entity Type

Business

Font styles to use
Serif
Other font styles liked:
• Atlanta

Colors
32a6d6
3277b5

Requirements
Must have
• Logo incorporated with all my stationery
• professional
Should not have
• Lots of colours
• Busy

```html
<!DOCTYPE html>
<html lang="en">
<head>
<meta charset="utf-8">
<title>Sumvane Financial Services – Stationery</title>
<link rel="stylesheet" href="https://fonts.googleapis.com/css2?family=Lato:wght@400;700&family=Cinzel:wght@500&display=swap">
<style>
:root{
  --bg:#c3c3c3;
  --paper:#ffffff;
  --brand:#1877c0;
  --brand-light:#32a6d6;
  --stripe-soft:#c6dcee;
  --stripe-mid:#7fb2dc;
  --ink:#222222;
  --body:#333333;
  --muted:#666666;
  --logo-ink:#4a4a4a;
}
*{box-sizing:border-box;margin:0;padding:0}
html,body{width:1200px;height:1200px;overflow:hidden}
body{background:var(--bg);font-family:"Lato",sans-serif;color:var(--ink);position:relative}
.sheet{position:absolute;background:var(--paper);overflow:hidden;box-shadow:6px 10px 18px rgba(0,0,0,.25)}
.card{width:257px;height:154px;border-radius:9px}

/* soft corner wash standing in for the angled band decoration */
.accent{position:absolute}
.accent-bl-strong{background:linear-gradient(30deg,var(--brand) 0%,rgba(24,119,192,.45) 45%,rgba(24,119,192,0) 75%)}
.accent-r-strong{background:linear-gradient(210deg,var(--brand) 0%,rgba(24,119,192,.45) 45%,rgba(24,119,192,0) 75%)}
.accent-bl-mid{background:linear-gradient(30deg,var(--stripe-mid) 0%,rgba(127,178,220,.45) 45%,rgba(127,178,220,0) 75%)}
.accent-bl-soft{background:linear-gradient(30deg,var(--stripe-soft) 0%,rgba(198,220,238,.5) 45%,rgba(198,220,238,0) 75%)}
.accent-flap{background:linear-gradient(0deg,var(--stripe-mid) 0%,rgba(127,178,220,0) 100%)}

.logo{position:absolute;display:flex;align-items:center;gap:7px}
.logo-mark{background:var(--brand-light);flex:none}
.logo-name{font-family:"Cinzel",serif;font-weight:500;color:var(--logo-ink);line-height:1}
.logo-name small{display:block;letter-spacing:.2em;margin-top:3px}
.person{position:absolute;left:23px;top:26px}
.person-name{color:var(--brand);font-size:9.5px}
.person-role{color:var(--muted);font-size:6.5px;margin-top:1px}
.contact{position:absolute;font-size:7.5px;line-height:10.5px;color:#444}
.contact .row{display:flex;align-items:center;gap:4px}
.contact .gap{height:5px}
.contact .addr{color:var(--ink)}
.dot{width:7px;height:7px;border-radius:50%;background:var(--brand);flex:none}
.divider{position:absolute;width:1px;background:#999}

.card-front-blue{background:var(--brand)}
.card-front-blue .logo-name{color:#fff}
.card-front-blue .logo-mark{background:#fff}

.letterhead{left:53px;top:258px;width:468px;height:663px}
.lh-to{position:absolute;left:41px;top:127px;font-size:8px;font-weight:700;line-height:16.6px}
.lh-body{position:absolute;left:41px;top:211px;width:392px;font-size:8.2px;line-height:16.6px;color:var(--body)}
.lh-body p{margin-bottom:16.6px}
.lh-sign{position:absolute;left:41px;top:477px;font-size:8.2px;color:var(--body)}
.signature{position:absolute;left:41px;top:494px;width:100px;height:44px;background:linear-gradient(90deg,#e8e8e8,#f4f4f4)}
.lh-sign-title{position:absolute;left:41px;top:543px;font-size:8.2px;color:var(--body)}
.lh-footer{position:absolute;left:67px;top:633px;display:flex;align-items:center;gap:14px;font-size:5.6px}
.lh-footer span{display:flex;align-items:center;gap:3px}
.lh-footer .dot{width:6px;height:6px}
.lh-footer .addr{color:var(--brand)}

.envelope-front{left:578px;top:268px;width:553px;height:261px}
.env-addr{position:absolute;left:145px;top:26px;font-size:8px;line-height:9.5px;padding-left:8px;border-left:1px solid var(--brand)}
.envelope-back{left:580px;top:558px;width:553px;height:261px}
.flap{position:absolute;left:0;top:0}
.comp-slip{left:585px;top:902px;width:459px;height:216px}
.comp-text{position:absolute;right:24px;bottom:10px;color:var(--brand);font-size:13.5px;letter-spacing:.02em}
</style>
</head>
<body>

<!-- Business card: back with contact -->
<div class="sheet card" style="left:53px;top:57px">
  <div class="person"><div class="person-name">Daniel Mercer</div><div class="person-role">Director</div></div>
  <div class="divider" style="left:147px;top:62px;height:73px"></div>
  <div class="contact" style="left:157px;top:62px">
    <div class="row"><i class="dot"></i>555-201-4470</div>
    <div class="row"><i class="dot"></i>555-201-4471</div>
    <div class="gap"></div>
    <div class="row"><i class="dot"></i>hello@sumvane.com.au</div>
    <div class="row"><i class="dot"></i>www.sumvane.com.au</div>
    <div class="gap"></div>
    <div class="addr">000 Harbour Street<br>WA 6000,xxxxxxx</div>
  </div>
  <div class="accent accent-bl-strong" style="left:0;top:96px;width:120px;height:58px" role="img" aria-label="Blue corner accent"></div>
</div>

<!-- Business card: blue front -->
<div class="sheet card card-front-blue" style="left:342px;top:60px">
  <div class="logo" style="left:35px;top:55px">
    <div class="logo-mark" style="width:18px;height:18px"></div>
    <div class="logo-name" style="font-size:28px">SUMVANE<small style="font-size:7px">FINANCIAL SERVICES</small></div>
  </div>
</div>

<!-- Business card: alternate back -->
<div class="sheet card" style="left:625px;top:58px">
  <div class="person"><div class="person-name">Daniel Mercer</div><div class="person-role">Director</div></div>
  <div class="contact" style="left:18px;top:66px">
    <div class="row"><i class="dot"></i>555-201-4470</div>
    <div class="row"><i class="dot"></i>555-201-4471</div>
    <div class="gap"></div>
    <div class="row"><i class="dot"></i>hello@sumvane.com.au</div>
    <div class="row"><i class="dot"></i>www.sumvane.com.au</div>
    <div class="gap"></div>
    <div class="addr">000 Harbour Street<br>WA 6000,xxxxxxx</div>
  </div>
  <div class="accent accent-r-strong" style="left:140px;top:42px;width:117px;height:70px" role="img" aria-label="Blue edge accent"></div>
</div>

<!-- Business card: white front -->
<div class="sheet card" style="left:913px;top:55px">
  <div class="logo" style="left:42px;top:58px">
    <div class="logo-mark" style="width:18px;height:18px"></div>
    <div class="logo-name" style="font-size:28px">SUMVANE<small style="font-size:7px">FINANCIAL SERVICES</small></div>
  </div>
</div>

<!-- Letterhead -->
<div class="sheet letterhead">
  <div class="logo" style="left:41px;top:36px">
    <div class="logo-mark" style="width:14px;height:14px"></div>
    <div class="logo-name" style="font-size:21px">SUMVANE<small style="font-size:6px">FINANCIAL SERVICES</small></div>
  </div>
  <div class="lh-to">To<br>Lorem Ipsum is simply<br>Lorem Ipsum is Lorem Ipsum is<br>Lorem Ipsum is</div>
  <div class="lh-body">
    <p>dummy text of the printing and typesetting industry. Lorem Ipsum has been the industry's standard dummy text ever since the 1500s, when an unknown printer took a galley of type and scrambled it to make a type specimen book. It has survived not only five centuries, but also the leap into electronic typesetting, remaining essentially unchanged.</p>
    <p>It is a long established fact that a reader will be distracted by the readable content of a page when looking at its layout. The point of using Lorem Ipsum is that it has a more-or-less normal distribution of letters, as opposed to using 'Content here, content here', making it look like readable English. Many desktop publishing packages and web page editors now use Lorem Ipsum as their default model text, and a search for 'lorem .</p>
    <p>Contrary to popular belief, Lorem Ipsum is not simply random text. It has roots in a piece of classical Latin literature from 45 BC, making it over 2000 years old. Martin Hale, a Latin professor at Northfield College in Ohio, looked up one of the more obscure Latin words, consectetur, from a Lorem Ipsum passage,</p>
  </div>
  <div class="lh-sign">Lorem Ipsum</div>
  <div class="signature" role="img" aria-label="Handwritten signature"></div>
  <div class="lh-sign-title">Lorem Ipsum is a dummy</div>
  <div class="accent accent-bl-soft" style="left:0;top:558px;width:215px;height:105px" role="img" aria-label="Soft blue corner accent"></div>
  <div class="lh-footer">
    <span><i class="dot"></i>55-201-4470</span>
    <span><i class="dot"></i>55-201-4471</span>
    <span><i class="dot"></i>www.sumvane.com.au</span>
    <span class="addr">|&nbsp;&nbsp;&nbsp;000 Harbour Street WA 6000,xxxxxxx</span>
  </div>
</div>

<!-- Envelope front -->
<div class="sheet envelope-front">
  <div class="logo" style="left:23px;top:24px">
    <div class="logo-mark" style="width:12px;height:12px"></div>
    <div class="logo-name" style="font-size:17px">SUMVANE<small style="font-size:4.8px">FINANCIAL SERVICES</small></div>
  </div>
  <div class="env-addr">000 Harbour Street<br>WA 6000,xxxxxxx</div>
  <div class="accent accent-bl-mid" style="left:0;top:174px;width:175px;height:87px" role="img" aria-label="Blue corner accent"></div>
</div>

<!-- Envelope back -->
<div class="sheet envelope-back">
  <svg class="flap" width="553" height="80" viewBox="0 0 553 80">
    <path d="M2,2 Q30,74 38,74 L515,74 Q523,74 550,2" fill="none" stroke="var(--brand)" stroke-width="0.8"/>
  </svg>
  <div class="accent accent-flap" style="left:172px;top:14px;width:120px;height:59px" role="img" aria-label="Blue flap accent"></div>
</div>

<!-- With compliments slip -->
<div class="sheet comp-slip">
  <div class="logo" style="left:19px;top:14px">
    <div class="logo-mark" style="width:11px;height:11px"></div>
    <div class="logo-name" style="font-size:14px">SUMVANE<small style="font-size:4px">FINANCIAL SERVICES</small></div>
  </div>
  <div class="accent accent-bl-soft" style="left:0;top:126px;width:185px;height:90px" role="img" aria-label="Soft blue corner accent"></div>
  <div class="comp-text">With Compliments</div>
</div>

</body>
</html>
```